Saltwater In store poster design

We need a poster design that will be hung in aquarium stores, to advertise that they use our natural saltwater.

Must use logo as well as be bright and colourful. We are trying to communicate that the water is natural (so good for your marine tank) as well as clean and safe, so please consider this in your design.

Must say something along the lines of "We use natural ocean water supplied by Reef Ready in our store" as well as "you can purchase natural ocean water here"

Open to all design types and suggestions as we will update the brief if we find one specific style that we prefer.

Target Market(s)

Customers who own marine aquariums

Industry/Entity Type

Store

Requirements
Must have
• Reef ready logo (does not need to have blue background attached, just the oval)

Be eye catching

Have similar phrases to those above

```html
<!DOCTYPE html>
<html lang="en">
<head>
<meta charset="utf-8">
<title>Natural Ocean Water – In-Store Poster</title>
<link href="https://fonts.googleapis.com/css2?family=Anton&family=Fredoka:wght@600&family=Quicksand:wght@400&display=swap" rel="stylesheet">
<style>
  :root {
    --page: #ffffff;
    --navy: #1e2f7a;
    --ocean: #0b4aa0;
    --ocean-bright: #1a8fe0;
    --sky: #8fd0f5;
    --ink: #0b4aa0;
    --frame: #222222;
    --white: #ffffff;
  }
  html, body {
    margin: 0;
    padding: 0;
    width: 1200px;
    height: 900px;
    overflow: hidden;
    background: var(--page);
  }
  .canvas {
    position: relative;
    width: 1200px;
    height: 900px;
  }
  .poster {
    position: absolute;
    left: 0;
    top: 0;
  }
  .headline-small {
    font-family: "Fredoka", "Arial Rounded MT Bold", sans-serif;
    font-weight: 600;
    fill: var(--ink);
  }
  .headline-big {
    font-family: "Anton", "Impact", sans-serif;
    filter: drop-shadow(0 0 6px var(--sky)) drop-shadow(0 0 3px var(--sky));
  }
  .supplied-by {
    font-family: "Quicksand", "Helvetica", sans-serif;
    font-weight: 400;
    fill: var(--white);
  }
  .brand-name {
    font-family: "Fredoka", "Arial Rounded MT Bold", sans-serif;
    font-weight: 600;
    fill: var(--white);
  }
</style>
</head>
<body>
<div class="canvas">
  <svg class="poster" width="1200" height="900" viewBox="0 0 1200 900" xmlns="http://www.w3.org/2000/svg">
    <defs>
      <linearGradient id="top-band" x1="0" y1="0" x2="1" y2="0">
        <stop offset="0" stop-color="var(--navy)"/>
        <stop offset="0.5" stop-color="var(--ocean-bright)"/>
        <stop offset="1" stop-color="var(--navy)"/>
      </linearGradient>
      <linearGradient id="water-fill" x1="0" y1="0" x2="0" y2="1">
        <stop offset="0" stop-color="#6cc4f0"/>
        <stop offset="0.45" stop-color="#2a86d4"/>
        <stop offset="1" stop-color="#0c3f95"/>
      </linearGradient>
      <clipPath id="poster-area">
        <rect x="295" y="27" width="608" height="858"/>
      </clipPath>
    </defs>

    <g clip-path="url(#poster-area)">
      <rect class="poster-sheet" x="295" y="27" width="608" height="858" fill="var(--page)"/>

      <path class="top-band" d="M295 27 H903 V98 Q640 20 295 75 Z" fill="url(#top-band)"/>

      <text class="headline-small" x="598" y="116" font-size="72" text-anchor="middle" textLength="300" lengthAdjust="spacingAndGlyphs">you can</text>
      <text class="headline-small" x="598" y="180" font-size="72" text-anchor="middle" textLength="345" lengthAdjust="spacingAndGlyphs">purchase</text>

      <g class="headline-big" fill="url(#water-fill)" role="img" aria-label="Water splash texture inside the lettering">
        <text x="597" y="333" font-size="158" text-anchor="middle" textLength="505" lengthAdjust="spacingAndGlyphs">natural</text>
        <text transform="translate(0 467) scale(1 1.42)" x="607" y="0" font-size="118" text-anchor="middle" textLength="490" lengthAdjust="spacingAndGlyphs">ocean</text>
        <text x="598" y="596" font-size="155" text-anchor="middle" textLength="480" lengthAdjust="spacingAndGlyphs">water</text>
      </g>

      <text class="headline-small" x="598" y="668" font-size="80" text-anchor="middle" textLength="178" lengthAdjust="spacingAndGlyphs">here</text>

      <path class="wave-band" fill="var(--ocean)"
        d="M295 716
           C320 712 340 700 365 692
           C395 684 410 702 430 712
           C460 724 490 700 530 698
           C570 696 590 712 630 708
           C670 704 700 688 740 692
           C790 696 810 716 850 712
           C875 710 890 700 903 704
           V885 H295 Z"/>

      <text class="supplied-by" x="367" y="815" font-size="35">supplied by</text>

      <circle class="brand-dot" cx="602" cy="800" r="12" fill="var(--white)"/>
      <text class="brand-name" x="625" y="818" font-size="50" textLength="240" lengthAdjust="spacingAndGlyphs">Reef Ready</text>
    </g>

    <rect class="poster-frame" x="295" y="27" width="608" height="858" fill="none" stroke="var(--frame)" stroke-width="1"/>
  </svg>
</div>
</body>
</html>
```